Brinevale Yacht Management Full Page Ad Flyer

Yacht Management Package also includes the following periodic Monthly services:

Monthly full vessel systems checklist inspections
Diver For Hull Cleaning And Inspection Of Props, Shafts, and Zincs
Interior/Exterior Detailing and scheduled washdowns
Manage Haulout
Pump-out Services
On-call Captain and Crew Services
Updates

Need more time to provide more content to designers and the printing press template file.

Target Market(s)

Vessel owners, motor yachts, sailboats from 25 feet in length up to 125 feet in length. We do not do cruise ships or yachts larger than 125 feet. Someone who has their boat docked at their house or a local marina. We also offer mobile on-site services.

```html
<!DOCTYPE html>
<html lang="en">
<head>
<meta charset="UTF-8">
<title>Brinevale Yacht Management – Full Page Ad</title>
<link rel="stylesheet" href="https://fonts.googleapis.com/css2?family=Bebas+Neue&family=Michroma&family=Roboto:wght@400&family=Yellowtail&display=swap">
<style>
  :root {
    --page-bg: #d6d6d6;
    --navy: #1f4aa0;
    --sky-blue: #2fa8e0;
    --panel: rgba(31, 74, 160, 0.93);
    --white: #ffffff;
    --tick: #3db4ea;
  }
  html, body {
    margin: 0;
    padding: 0;
    width: 1200px;
    height: 2201px;
    overflow: hidden;
    background: var(--page-bg);
  }
  .flyer {
    position: absolute;
    left: 50px;
    top: 337px;
    width: 1100px;
    height: 1526px;
    overflow: hidden;
    box-shadow: 0 6px 24px rgba(0, 0, 0, 0.18);
  }
  .flyer-photo {
    position: absolute;
    inset: 0;
    background:
      linear-gradient(90deg, rgba(255,255,255,0) 60%, rgba(240,236,232,0.55) 78%, rgba(190,150,120,0.35) 100%),
      linear-gradient(180deg, #eef2f4 0%, #dde8ef 35%, #c9dce8 52%, #3f86b0 62%, #246391 80%, #1a4f74 100%);
  }
  .brand-name {
    position: absolute;
    left: 0;
    width: 638px;
    top: 108px;
    margin: 0;
    text-align: center;
    font-family: "Michroma", sans-serif;
    font-size: 24px;
    letter-spacing: 4px;
    color: var(--navy);
    text-transform: uppercase;
  }
  .headline {
    position: absolute;
    left: 0;
    top: 0;
    width: 1100px;
    height: 760px;
    margin: 0;
  }
  .headline-script { font-family: "Yellowtail", cursive; fill: var(--navy); }
  .headline-main { font-family: "Bebas Neue", sans-serif; fill: var(--sky-blue); }
  .headline-sub { font-family: "Michroma", sans-serif; font-weight: 700; fill: var(--navy); }
  .services-panel {
    position: absolute;
    left: 118px;
    top: 754px;
    width: 628px;
    height: 710px;
    background: var(--panel);
    box-sizing: border-box;
    padding: 36px 0 0 78px;
  }
  .services-title {
    margin: 0;
    font-family: "Michroma", sans-serif;
    font-weight: 400;
    font-size: 50px;
    line-height: 66px;
    color: var(--white);
    letter-spacing: 2px;
  }
  .services-list {
    list-style: none;
    margin: 40px 0 0 0;
    padding: 0;
  }
  .services-list li {
    position: relative;
    padding-left: 42px;
    margin-bottom: 18px;
    font-family: "Roboto", sans-serif;
    font-size: 22px;
    line-height: 27px;
    color: var(--white);
  }
  .services-list .tick {
    position: absolute;
    left: 0;
    top: 5px;
    width: 16px;
    height: 16px;
  }
</style>
</head>
<body>
  <main class="flyer">
    <div class="flyer-photo" role="img" aria-label="Photo of a white luxury yacht's teak side deck and railing running along the right, with open blue sea and a bright hazy sky"></div>

    <p class="brand-name">Brinevale Yacht Management</p>

    <svg class="headline" viewBox="0 0 1100 760" aria-labelledby="headline-text">
      <title id="headline-text">Yacht Management Package</title>
      <text class="headline-script" x="108" y="415" font-size="300">Yacht</text>
      <text class="headline-main" x="189" y="640" font-size="186" textLength="627" lengthAdjust="spacingAndGlyphs">MANAGEMENT</text>
      <text class="headline-sub" x="225" y="733" font-size="54" textLength="608" lengthAdjust="spacing">PACKAGE</text>
    </svg>

    <section class="services-panel">
      <h2 class="services-title">MONTHLY<br>SERVICES:</h2>
      <ul class="services-list">
        <li><svg class="tick" viewBox="0 0 16 16"><circle cx="8" cy="8" r="8" fill="var(--tick)"/><path d="M4.5 8.2l2.3 2.3 4.6-4.6" fill="none" stroke="#fff" stroke-width="1.8"/></svg>Monthly full vessel<br>systems checklist inspections</li>
        <li><svg class="tick" viewBox="0 0 16 16"><circle cx="8" cy="8" r="8" fill="var(--tick)"/><path d="M4.5 8.2l2.3 2.3 4.6-4.6" fill="none" stroke="#fff" stroke-width="1.8"/></svg>Diver For Hull Cleaning And Inspection<br>Of Props, Shafts, and Zincs</li>
        <li><svg class="tick" viewBox="0 0 16 16"><circle cx="8" cy="8" r="8" fill="var(--tick)"/><path d="M4.5 8.2l2.3 2.3 4.6-4.6" fill="none" stroke="#fff" stroke-width="1.8"/></svg>Interior/Exterior Detailing and scheduled<br>washdowns</li>
        <li><svg class="tick" viewBox="0 0 16 16"><circle cx="8" cy="8" r="8" fill="var(--tick)"/><path d="M4.5 8.2l2.3 2.3 4.6-4.6" fill="none" stroke="#fff" stroke-width="1.8"/></svg>Manage Haulout</li>
        <li><svg class="tick" viewBox="0 0 16 16"><circle cx="8" cy="8" r="8" fill="var(--tick)"/><path d="M4.5 8.2l2.3 2.3 4.6-4.6" fill="none" stroke="#fff" stroke-width="1.8"/></svg>Pump-out Services</li>
        <li><svg class="tick" viewBox="0 0 16 16"><circle cx="8" cy="8" r="8" fill="var(--tick)"/><path d="M4.5 8.2l2.3 2.3 4.6-4.6" fill="none" stroke="#fff" stroke-width="1.8"/></svg>On-call Captain and Crew Services</li>
      </ul>
    </section>
  </main>
</body>
</html>
```